Roles For Metrics - Job Board for Big Data Professionals

Hi all,

I need a design for a job board I'm kicking off that is focused on finding jobs and people that work in Data Analytics.

I've attached a fairly in depth design spec and wireframe giving a rough mockup. Please note that in the wireframe, the boxes are there to demonstrate orders of content. This is not to say that a lot of distinct content boxes will necessarily be the best way of presenting content.

I will be available on Chatterlink (marcus.wendholt) and email (w3ndh0lt@quillpost.net) and will give constant and clear feedback on the way.

Payment is not guaranteed yet. As soon as there are at least 5+ promising designs I will make this guaranteed.

Thanks
Marcus
Updates

Hi all

Please suspend all work on this project for the time being.

I am working closely with 1 designer who I will very likely accept their design.

I appreciate all the work you have put into this, but dont want to waste any more of your time.

Thanks
Marcus

Industry/Entity Type

Work

Requirements
Must have
• I'd like a clean, modern web design which has strong use of Typography. Strong use of a clear and consistent palette of colours.
Should not have
• Boxes with rounded edges

```html
<!DOCTYPE html>
<html lang="en">
<head>
<meta charset="utf-8">
<title>Roles For Metrics – Job Board</title>
<link rel="stylesheet" href="https://fonts.googleapis.com/css2?family=Open+Sans:wght@400;600;700&family=Arimo:wght@400;700&family=Hind:wght@400;500&display=swap">
<style>
:root{
  --ink:#222;
  --muted:#666;
  --nav:#2b2b2b;
  --login-red:#b01200;
  --search-orange:#ff4a00;
  --news-purple:#a23aa8;
  --alert-blue:#6b75c9;
  --rec-dark:#b01424;
  --rec:#cf3040;
  --grad-dark:#007a80;
  --grad:#00a0b0;
  --promo-pink:#e07fa8;
  --chirp-gold:#d4ac2e;
  --panel:#f7f7f7;
  --line:#cfcfcf;
  --jobseeker-blue:#0a6fa8;
  --accent-red:#b01b1b;
}
*{box-sizing:border-box;margin:0;padding:0}
html,body{width:1200px;height:1004px;overflow:hidden;background:#fff}
body{font-family:"Arimo",Arial,sans-serif;color:var(--ink)}
.stage{position:absolute;left:0;top:0;width:1152px;height:960px;transform:scale(1.0417,1.0458);transform-origin:0 0}
.sheet{position:absolute;left:52px;top:0;width:1048px;height:960px;background:#fff;box-shadow:0 0 18px rgba(0,0,0,.12)}
.abs{position:absolute}
.brand{left:85px;top:44px;display:flex;align-items:center;gap:8px}
.brand-mark{width:34px;height:34px;background:var(--login-red)}
.brand-name{font-family:"Hind",sans-serif;font-size:34px;font-weight:400;color:var(--ink);letter-spacing:1px;line-height:1}
.banner{left:536px;top:7px;width:540px;height:89px;border:1px solid #e8a8e0;background:linear-gradient(90deg,#fff 55%,#fbe9f3 70%,#3cb8c8 82%,#f0c030 92%,#e83070)}
.banner span{position:absolute;left:10px;top:30px;font-family:Georgia,serif;font-size:24px;color:#1aa88a;letter-spacing:.5px}
.nav{left:76px;top:102px;width:1000px;height:42px;background:var(--nav);display:flex;align-items:center;padding-left:12px}
.nav a{color:#fff;font-family:"Open Sans",sans-serif;font-size:12.5px;text-decoration:none;padding:0 10px;border-right:1px dashed #777;line-height:20px}
.nav a:last-of-type{border-right:1px dashed #777}
.nav .search{position:absolute;left:662px;top:10px;width:324px;height:23px;background:#eee;font-size:12px;color:#333;padding:4px 30px;letter-spacing:.5px}
.nav .search svg{position:absolute;right:14px;top:4px}
.panel{top:146px;height:205px;color:#fff}
.panel h2{font-family:"Hind",sans-serif;font-weight:400;font-size:22px;position:absolute;left:22px;top:14px;display:flex;align-items:center;gap:10px}
.field{position:absolute;background:#fff;color:#111;font-size:11px;padding:8px 9px;height:28px}
.btn{position:absolute;background:#000;color:#fff;font-size:12px;padding:6px 15px;height:27px}
.small{position:absolute;font-size:11px;line-height:14px}
.login{left:76px;width:280px;background:var(--login-red)}
.jobsearch{left:357px;width:365px;background:var(--search-orange)}
.news{left:724px;width:352px;background:var(--news-purple)}
.news .feed{position:absolute;left:16px;top:52px;width:300px;font-size:11px;line-height:13px}
.news .feed p{margin-bottom:14px}
.scroll{position:absolute;right:2px;top:6px;width:16px;height:198px;background:#f2f2f2;border:1px solid #ccc}
.scroll i{position:absolute;left:1px;top:16px;width:12px;height:58px;background:#c8d4f0;border:1px solid #9ab}
.alert{left:76px;top:353px;width:1000px;height:45px;background:var(--alert-blue);color:#222;font-family:"Open Sans",sans-serif;font-size:13px}
.alert .input{position:absolute;top:10px;height:26px;background:#fff;font-size:10px;padding:7px 14px;color:#111}
.why{left:76px;top:408px;width:457px;height:291px;border:1px solid var(--line);padding:6px}
.why-inner{background:var(--panel);height:100%;padding:12px 14px}
.why h1{font-family:"Open Sans",sans-serif;font-weight:400;font-size:20px;margin-bottom:10px}
.why p{font-size:11px;line-height:13px;width:400px}
.cols{display:flex;margin-top:18px}
.col{width:200px}
.col h3{font-family:"Open Sans",sans-serif;font-weight:400;font-size:15px;margin-bottom:12px}
.col.seek h3{color:var(--jobseeker-blue)}.col.rec h3{color:var(--accent-red)}
.col li{list-style:none;font-size:11px;line-height:13px;padding-left:13px;position:relative;margin-bottom:14px}
.col li::before{content:"";position:absolute;left:0;top:4px;width:5px;height:5px;border-radius:50%}
.seek li::before{background:var(--jobseeker-blue)}.rec li::before{background:var(--accent-red)}
.promo h4{font-family:"Open Sans",sans-serif;font-weight:400;font-size:15px;color:#fff;padding:9px 18px;height:36px}
.promo .word{position:absolute;font-family:"Open Sans",sans-serif;font-weight:700;font-size:21px;color:#fff;text-shadow:2px 2px 2px rgba(0,0,0,.35)}
.recruiters{left:540px;top:407px;width:229px;height:149px;background:var(--rec)}
.recruiters h4{background:var(--rec-dark)}
.graduates{left:540px;top:568px;width:229px;height:131px;background:var(--grad)}
.graduates h4{background:var(--grad-dark)}
.featured-title{left:777px;top:420px;font-family:"Open Sans",sans-serif;font-size:15px;color:#222}
.featured{left:776px;top:449px;width:300px;height:250px;background:linear-gradient(160deg,#e98fb5,var(--promo-pink) 60%,#d86d9a)}
.chirp{left:76px;top:709px;width:1000px;height:69px;background:var(--chirp-gold);color:#fff}
.chirp .mark{position:absolute;left:11px;top:12px;width:47px;height:43px;background:#fff;color:var(--chirp-gold);font-family:"Open Sans",sans-serif;font-size:10px;font-weight:700;display:flex;align-items:center;justify-content:center}
.chirp p{position:absolute;left:74px;top:20px;width:820px;font-family:"Open Sans",sans-serif;font-size:11px;line-height:15px;font-weight:600}
.footer-col{top:805px;font-size:11px;line-height:13px;color:var(--muted)}
.footer-col b{color:#333}
</style>
</head>
<body>
<div class="stage">
  <div class="sheet"></div>

  <div class="abs brand"><span class="brand-mark"></span><span class="brand-name">METRIVA</span></div>
  <div class="abs banner"><span>AD BANNER SPACE</span></div>

  <nav class="abs nav">
    <a>HOME</a><a>JOBS</a><a>ACCOUNT</a><a>REGISTER</a><a>NEWS &amp; INSIGHT</a><a>GRADUATES</a><a>RECRUITERS</a><a>ABOUT</a>
    <div class="search">enter keywords and search
      <svg width="16" height="14" viewBox="0 0 16 14"><circle cx="6" cy="6" r="4.5" fill="none" stroke="#222" stroke-width="1.8"/><line x1="9.5" y1="9" x2="14" y2="13" stroke="#222" stroke-width="2.4"/></svg>
    </div>
  </nav>

  <section class="abs panel login">
    <h2>account login
      <svg width="50" height="14" viewBox="0 0 50 14"><circle cx="7" cy="7" r="5" fill="none" stroke="#fff" stroke-width="2"/><path d="M12 7H48M40 7v5M44 7v5M47 7v4" stroke="#fff" stroke-width="2" fill="none"/></svg>
    </h2>
    <div class="field" style="left:24px;top:58px;width:187px">username</div>
    <div class="field" style="left:24px;top:99px;width:187px">password</div>
    <div class="btn" style="left:24px;top:140px">sign in</div>
    <div class="small" style="left:121px;top:141px">Keep me signed in<br>Forgot Your Password?<br>Registration</div>
  </section>

  <section class="abs panel jobsearch">
    <h2>job search category
      <svg width="34" height="28" viewBox="0 0 34 28"><circle cx="11" cy="11" r="8" fill="none" stroke="#fff" stroke-width="3"/><line x1="17" y1="17" x2="30" y2="26" stroke="#fff" stroke-width="4"/></svg>
    </h2>
    <div class="field" style="left:21px;top:58px;width:147px">keywords</div>
    <div class="field" style="left:181px;top:58px;width:147px">city search</div>
    <div class="field" style="left:21px;top:98px;width:147px">keywords</div>
    <div class="field" style="left:181px;top:98px;width:147px">categories</div>
    <div class="small" style="left:20px;top:142px">Advanced search<br>Search by Company</div>
    <div class="btn" style="left:258px;top:140px">sign in</div>
    <div class="small" style="left:20px;top:182px;color:#111;font-weight:700">8 jobs currently online. 3 resumes currently online.</div>
  </section>

  <section class="abs panel news">
    <h2 style="left:15px">latest news<small style="font-size:13px">&amp;</small> insight
      <svg width="44" height="34" viewBox="0 0 44 34"><path d="M3 12h7l10-9v28l-10-9H3z" fill="none" stroke="#fff" stroke-width="1.6"/><path d="M26 11q4 6 0 12M31 7q7 10 0 20M36 3q10 14 0 28" fill="none" stroke="#fff" stroke-width="1.6"/></svg>
    </h2>
    <div class="feed">
      <p><b>2011-09-28</b><br>The Newest 3.4 Version of HireGrid Software is Released!</p>
      <p>HireGrid team informs about the launch of the newest 3.4 software version.</p>
      <p><b style="font-weight:400">2011-09-28</b><br>The Newest 3.4 Version of HireGrid Software is Released!</p>
    </div>
    <div class="scroll"><i></i></div>
  </section>

  <section class="abs alert">
    <svg class="abs" style="left:17px;top:14px" width="26" height="18" viewBox="0 0 26 18"><rect x="1" y="1" width="24" height="16" fill="none" stroke="#222" stroke-width="1.4"/><path d="M1 1l12 9 12-9" fill="none" stroke="#222" stroke-width="1.4"/></svg>
    <span class="abs" style="left:50px;top:14px">email alert</span>
    <div class="input" style="left:117px;width:290px">enter your email address</div>
    <svg class="abs" style="left:414px;top:11px" width="24" height="24" viewBox="0 0 24 24"><circle cx="12" cy="12" r="10.5" fill="#fff" stroke="#222"/><path d="M8 6l7 6-7 6" fill="none" stroke="#222" stroke-width="1.6"/></svg>
    <svg class="abs" style="left:532px;top:9px" width="12" height="28" viewBox="0 0 12 28"><path d="M4 24V6a3 3 0 016 0v17a4.5 4.5 0 01-9 0V9" fill="none" stroke="#222" stroke-width="1.4"/></svg>
    <span class="abs" style="left:550px;top:14px">post your resume</span>
    <div class="input" style="left:657px;width:290px"></div>
    <svg class="abs" style="left:925px;top:13px" width="20" height="20" viewBox="0 0 20 20"><rect width="20" height="20" fill="#1e88d8"/><path d="M4 10h10M10 5l5 5-5 5" fill="none" stroke="#fff" stroke-width="2.4"/></svg>
  </section>

  <section class="abs why">
    <div class="why-inner">
      <h1>Why Roles For Metrics?</h1>
      <p>Lorem ipsum dolor sit amet, consectetur adipiscing elit. Quisque et iaculis metus. Donec nisl eros, auctor nec blandit et, dignissim sit amet augue. Nulla facilisi. Morbi id sem nibh, sit amet tristique tortor. Etiam at tellus ullamcorper quam hendrerit cursus. Maecenas in tellus nunc, eget lobortis quam. Aliquam vel consectetur orci.</p>
      <div class="cols">
        <ul class="col seek"><h3>JOBSEEKERS</h3>
          <li>Lorem ipsum dolor sit amet, consectetur adipiscing elit.</li>
          <li>Lorem ipsum dolor sit amet, consectetur adipiscing elit.</li>
          <li>Lorem ipsum dolor sit amet, consectetur adipiscing elit.</li>
        </ul>
        <ul class="col rec"><h3>RECRUITERS</h3>
          <li>Lorem ipsum dolor sit amet, consectetur adipiscing elit.</li>
          <li>Lorem ipsum dolor sit amet, consectetur adipiscing elit.</li>
          <li>Lorem ipsum dolor sit amet, consectetur adipiscing elit.</li>
        </ul>
      </div>
    </div>
  </section>

  <section class="abs promo recruiters">
    <h4>FOR RECRUITERS</h4>
    <span class="word" style="left:18px;top:38px">login</span>
    <span class="word" style="left:70px;top:72px">search resume</span>
    <span class="word" style="left:20px;top:106px;color:#19a0d8">advertise</span>
  </section>

  <section class="abs promo graduates">
    <h4>FOR GRADUATES</h4>
    <span class="word" style="left:18px;top:48px;color:#ff5a1a">login</span>
    <span class="word" style="left:80px;top:68px;color:#e8186a">post resume</span>
  </section>

  <div class="abs featured-title">FEATURED PARTNER ADVERTISEMENT</div>
  <div class="abs featured" role="img" aria-label="Partner advertisement for the Tunelet music player: silhouette of a dancer listening on headphones against a pink backdrop"></div>

  <section class="abs chirp">
    <div class="mark">Chirper</div>
    <p>Welcome to HireGrid! This is the test blog post. To edit/delete it or add new posts you need to go to /blogdesk/ and sign in using the .log in. link at the bottom of the page. Testing the demo blog Thank you!</p>
  </section>

  <div class="abs footer-col" style="left:82px"><b>Stay in touch</b><br>Contact us<br>Careers<br>Partner Portal<br>Email sign up<br>RSS Feeds<br>LinkedUp<br>Friendbook<br>Follow us on Chirper</div>
  <div class="abs footer-col" style="left:252px"><b>Stay in touch</b><br>Contact us<br>Careers<br>Partner Portal<br>Email sign up<br>RSS Feeds<br>LinkedUp<br>Friendbook<br>Follow us on Chirper</div>
  <div class="abs footer-col" style="left:415px"><b>Stay in touch</b><br>Contact us<br>Careers<br>Partner Portal<br>Email sign up<br>RSS Feeds<br>LinkedUp<br>Friendbook<br>Follow us on Chirper</div>
  <div class="abs footer-col" style="left:585px"><b>Stay in touch</b><br>Contact us<br>Careers<br>Partner Portal<br>Email sign up<br>RSS Feeds<br>LinkedUp<br>Friendbook<br>Follow us on Chirper</div>
  <div class="abs footer-col" style="left:765px"><b>Stay in touch</b><br>Contact us<br>Careers<br>Partner Portal<br>Email sign up<br>RSS Feeds<br>LinkedUp<br>Friendbook<br>Follow us on Chirper</div>
  <div class="abs footer-col" style="left:935px"><b>Stay in touch</b><br>Contact us<br>Careers<br>Partner Portal<br>Email sign up<br>RSS Feeds<br>LinkedUp<br>Friendbook<br>Follow us on Chirper</div>
</div>
</body>
</html>
```